Flyer for Brand New Montessori School

Quiet Harbor Academy is opening in the fall to students infant-5th grade. We need a catchy, professional flyer that will attract a very upscale clientele. Most of our students will be under the age of 5, but we want to attract older students as well. The project is to design a flyer that tells people about our school, and directs them to the website to enroll/get more information

Target Market(s)

Upscale, affluent parents who need care for and want to educate their children starting at a young age.

Industry/Entity Type

Education/Day Care

Font styles to use
Serif

Colors
59FF00
82FF00
B8FF75
E3FFCB
F4FFEA
6B429C
8869AF
B7A5CE
E3DAEB
F3F0F8

Requirements
Must have
• photos of children, a clean look
Nice to have
• Please see attached logo samples. I am going to use either 2a or 4a; those are the colors i would like to use
Should not have
• A cluttered look or too much information

```html
<!DOCTYPE html>
<html lang="en">
<head>
<meta charset="utf-8">
<title>Quiet Harbor Academy Flyer</title>
<link href="https://fonts.googleapis.com/css2?family=Catamaran:wght@400;500;600;700;800&display=swap" rel="stylesheet">
<style>
  :root{
    --purple:#512A6E;
    --purple-soft:#7A5A98;
    --green:#23A24A;
    --green-dark:#1E8C46;
    --orange:#E0642A;
    --grey:#8A8A8A;
    --paper:#F1F6EF;
    --white:#FFFFFF;
    --ink:#111111;
  }
  *{box-sizing:border-box;margin:0;padding:0}
  html,body{width:866px;height:1200px;overflow:hidden;background:var(--paper)}
  body{font-family:"Catamaran",Arial,sans-serif;color:var(--ink)}
  .flyer{position:relative;width:866px;height:1200px;background:var(--paper);overflow:hidden}
  .abs{position:absolute}

  .hero{position:absolute;left:0;top:0}

  .brand{left:40px;top:410px;display:flex;align-items:center;gap:10px}
  .brand-dot{width:44px;height:44px;border-radius:50%;background:var(--purple)}
  .brand-name{font-weight:800;font-size:27px;line-height:26px;color:var(--purple);letter-spacing:.5px}

  .about{left:41px;top:495px;width:248px;height:289px;background:var(--purple);border-radius:14px;color:var(--white);text-align:center;padding:26px 12px 0;font-size:13.6px;line-height:17px}
  .about p+p{margin-top:9px}
  .about strong{font-weight:700}

  .divider{left:299px;top:312px;width:1px;height:410px;background:#9c8fab}

  .headline{left:309px;top:315px;font-size:35px;line-height:42px;font-weight:800;color:var(--green);letter-spacing:-.3px}
  .subhead{left:309px;top:403px;font-size:20.5px;font-weight:700;color:var(--purple);letter-spacing:-.3px}
  .intro{left:309px;top:443px;width:510px;font-size:11.6px;line-height:15.5px;font-weight:700;color:var(--ink)}
  .section-title{left:309px;top:483px;font-size:14.5px;font-weight:800;color:var(--green)}
  .section-rule{left:480px;top:493px;width:326px;height:1px;background:#8fd3a3}

  .tabs{left:309px;top:507px}
  .tab-label{position:absolute;font-size:10px;font-weight:700;color:var(--white);text-align:center;line-height:11px}

  .col{top:550px;font-size:11.4px;line-height:14.6px;list-style:none}
  .col li{position:relative;padding-left:12px}
  .col li::before{content:"";position:absolute;left:1px;top:6px;width:3.5px;height:3.5px;border-radius:50%;background:currentColor}
  .col-program{left:312px;width:172px;color:var(--purple)}
  .col-family{left:488px;width:175px;color:var(--green)}
  .col-team{left:665px;width:160px;color:var(--grey)}

  .community{left:0;top:814px;width:866px;height:313px;background:var(--purple)}
  .banner{left:139px;top:791px;width:588px;height:47px;border-radius:24px;background:linear-gradient(90deg,#22A24A 0%,#5A3A7A 45%,#8A3D7A 65%,#F07A22 100%);color:var(--white);font-weight:800;font-size:18px;text-align:center;line-height:49px;letter-spacing:-.3px}

  .checks{list-style:none;font-size:11.6px;line-height:13.5px;color:var(--white)}
  .checks li{position:relative;padding-left:15px;margin-bottom:4.5px}
  .checks li svg{position:absolute;left:0;top:1px}
  .checks-staff{left:40px;top:939px;width:240px}
  .checks-students{left:583px;top:868px;width:230px}
  .checks-families{left:583px;top:1010px;width:235px}
  .dotted{left:597px;top:977px;width:213px;border-top:1px dotted #cfc3dc}

  .circle-label{position:absolute;font-size:14.5px;font-weight:700;text-align:center;width:120px}

  .footer-line{left:0;top:1127px;width:866px;height:6px;background:var(--white)}
  .footer{left:0;top:1133px;width:866px;height:67px;background:var(--green);color:var(--white);font-size:18px;text-align:center;line-height:72px}
  .footer b{font-weight:700}
  .globe{left:409px;top:1103px}
</style>
</head>
<body>
<main class="flyer">

  <svg class="hero" width="866" height="368" viewBox="0 0 866 368">
    <defs>
      <linearGradient id="photoTone" x1="0" y1="0" x2="0" y2="1">
        <stop offset="0" stop-color="#2E7A4E"/>
        <stop offset=".55" stop-color="#6E9E7C"/>
        <stop offset="1" stop-color="#C9A58A"/>
      </linearGradient>
    </defs>
    <polygon points="0,0 866,0 866,307 303,307 220,367 0,367" fill="url(#photoTone)" role="img" aria-label="Photo of smiling school children with their teacher in front of a green chalkboard"/>
    <polygon points="303,307 316,307 233,367 220,367" fill="var(--purple)"/>
    <polygon points="316,307 320,307 237,367 233,367" fill="var(--white)"/>
  </svg>

  <div class="abs brand">
    <span class="brand-dot"></span>
    <span class="brand-name">QUIET<br>HARBOR<br>ACADEMY</span>
  </div>

  <div class="abs about">
    <p><strong>Quiet Harbor Academy</strong><br>educates infant through 5th grade students, utilizing the renowned Montessori approach to education. Montessori education help students develop skills and talents that lead to incredible future success.</p>
    <p>Our students achieve academic excellence, learn independence, discover a natural love for learning and develop respect for self and others and a global mindset.</p>
  </div>

  <div class="abs divider"></div>

  <h1 class="abs headline">Give your child an advanced start<br>at Quiet Harbor Academy!</h1>
  <h2 class="abs subhead">Montessori Education for Tomorrow’s Global Leaders</h2>
  <p class="abs intro">We employ a research-based, neurologically informed educational program that promotes brain development, social skills, problem solving and creativity.</p>

  <h3 class="abs section-title">OUR DIFFERENTIATION</h3>
  <div class="abs section-rule"></div>

  <div class="abs tabs">
    <svg width="516" height="32" viewBox="0 0 516 32">
      <polygon points="360,0 505,0 516,16 505,32 360,32 371,16" fill="#8A8A8A"/>
      <polygon points="166,0 357,0 368,16 357,32 166,32 177,16" fill="var(--green)"/>
      <polygon points="0,0 163,0 175,16 163,32 0,32" fill="var(--purple)"/>
      <polygon points="163,0 166,0 178,16 166,32 163,32 175,16" fill="var(--white)"/>
      <polygon points="357,0 360,0 372,16 360,32 357,32 369,16" fill="var(--white)"/>
    </svg>
    <span class="tab-label" style="left:8px;top:5px;width:150px">Customized Educational<br>Program</span>
    <span class="tab-label" style="left:190px;top:10px;width:150px">Family Support</span>
    <span class="tab-label" style="left:375px;top:10px;width:125px">Top Notch Team</span>
  </div>

  <ul class="abs col col-program">
    <li>Begin with infants-utilize every precious moment</li>
    <li>Montessori Curriculum</li>
    <li>Critical thinking, Creativity, Academic Skill</li>
    <li>Problem Solving, Language, Compassion</li>
    <li>Research and Neurologically based</li>
  </ul>
  <ul class="abs col col-family">
    <li>Welcoming atmosphere for parents as partners</li>
    <li>Provide answers for parents in all areas of parenting</li>
    <li>Create community of like-minded parents</li>
    <li>High levels of customer service</li>
    <li>Engage other caring adults and multi-generational families</li>
    <li>Redefine expectations for education</li>
    <li>Help student acheive potential</li>
  </ul>
  <ul class="abs col col-team">
    <li>Talented, best in class professional teachers</li>
    <li>Team that is balanced around desired characteristics</li>
    <li>Opportunity to provide input and shape future of the school</li>
    <li>Great compensation, profit sharing and robust professional development opportunities</li>
    <li>Experienced school leader with 25+ years experience in best schools in the country</li>
  </ul>

  <section class="abs community"></section>
  <div class="abs banner">JOIN A COMMUNITY OF PARENTS JUST LIKE YOU!</div>

  <svg class="abs" style="left:0;top:814px" width="866" height="313" viewBox="0 814 866 313">
    <line x1="279" y1="950" x2="279" y2="1008" stroke="#B27A8A" stroke-width="1"/>
    <line x1="279" y1="977" x2="320" y2="977" stroke="#B27A8A" stroke-width="1"/>
    <line x1="575" y1="872" x2="575" y2="940" stroke="#B7A5CE" stroke-width="1"/>
    <line x1="545" y1="906" x2="575" y2="906" stroke="#B7A5CE" stroke-width="1"/>
    <line x1="575" y1="1012" x2="575" y2="1090" stroke="#B7A5CE" stroke-width="1"/>
    <line x1="545" y1="1045" x2="575" y2="1045" stroke="#B7A5CE" stroke-width="1"/>
    <circle cx="383" cy="977" r="64" fill="var(--orange)"/>
    <circle cx="481" cy="924" r="64" fill="#E3DAEB" fill-opacity=".9"/>
    <circle cx="481" cy="1030" r="64" fill="var(--green-dark)" fill-opacity=".95"/>
  </svg>
  <span class="circle-label" style="left:421px;top:912px;color:var(--purple)">Students</span>
  <span class="circle-label" style="left:323px;top:1072px;top:965px;color:var(--white)">Staff</span>
  <span class="circle-label" style="left:421px;top:1024px;color:var(--white)">Families</span>

  <ul class="abs checks checks-staff">
    <li><svg width="10" height="10" viewBox="0 0 10 10"><circle cx="5" cy="5" r="5" fill="var(--orange)"/><path d="M2.7 5.2 4.3 6.7 7.3 3.6" stroke="#fff" stroke-width="1.3" fill="none"/></svg>Strengths and unique abilities leveraged</li>
    <li><svg width="10" height="10" viewBox="0 0 10 10"><circle cx="5" cy="5" r="5" fill="var(--orange)"/><path d="M2.7 5.2 4.3 6.7 7.3 3.6" stroke="#fff" stroke-width="1.3" fill="none"/></svg>Valued as professionals</li>
    <li><svg width="10" height="10" viewBox="0 0 10 10"><circle cx="5" cy="5" r="5" fill="var(--orange)"/><path d="M2.7 5.2 4.3 6.7 7.3 3.6" stroke="#fff" stroke-width="1.3" fill="none"/></svg>Mutual Investment</li>
    <li><svg width="10" height="10" viewBox="0 0 10 10"><circle cx="5" cy="5" r="5" fill="var(--orange)"/><path d="M2.7 5.2 4.3 6.7 7.3 3.6" stroke="#fff" stroke-width="1.3" fill="none"/></svg>Close relationship with students and families</li>
  </ul>

  <ul class="abs checks checks-students">
    <li><svg width="10" height="10" viewBox="0 0 10 10"><circle cx="5" cy="5" r="5" fill="#fff"/><path d="M2.7 5.2 4.3 6.7 7.3 3.6" stroke="var(--purple)" stroke-width="1.3" fill="none"/></svg>Challenged and loved</li>
    <li><svg width="10" height="10" viewBox="0 0 10 10"><circle cx="5" cy="5" r="5" fill="#fff"/><path d="M2.7 5.2 4.3 6.7 7.3 3.6" stroke="var(--purple)" stroke-width="1.3" fill="none"/></svg>Close Relationship with Teachers</li>
    <li><svg width="10" height="10" viewBox="0 0 10 10"><circle cx="5" cy="5" r="5" fill="#fff"/><path d="M2.7 5.2 4.3 6.7 7.3 3.6" stroke="var(--purple)" stroke-width="1.3" fill="none"/></svg>Alignment between school, home and family</li>
    <li><svg width="10" height="10" viewBox="0 0 10 10"><circle cx="5" cy="5" r="5" fill="#fff"/><path d="M2.7 5.2 4.3 6.7 7.3 3.6" stroke="var(--purple)" stroke-width="1.3" fill="none"/></svg>Personalized learning at own pace</li>
  </ul>
  <div class="abs dotted"></div>
  <ul class="abs checks checks-families">
    <li><svg width="10" height="10" viewBox="0 0 10 10"><circle cx="5" cy="5" r="5" fill="#7BCB8E"/><path d="M2.7 5.2 4.3 6.7 7.3 3.6" stroke="#fff" stroke-width="1.3" fill="none"/></svg>School sets and meets high expectations</li>
    <li><svg width="10" height="10" viewBox="0 0 10 10"><circle cx="5" cy="5" r="5" fill="#7BCB8E"/><path d="M2.7 5.2 4.3 6.7 7.3 3.6" stroke="#fff" stroke-width="1.3" fill="none"/></svg>Welcomed and invited to engage</li>
    <li><svg width="10" height="10" viewBox="0 0 10 10"><circle cx="5" cy="5" r="5" fill="#7BCB8E"/><path d="M2.7 5.2 4.3 6.7 7.3 3.6" stroke="#fff" stroke-width="1.3" fill="none"/></svg>High levels of service and educational concierge</li>
    <li><svg width="10" height="10" viewBox="0 0 10 10"><circle cx="5" cy="5" r="5" fill="#7BCB8E"/><path d="M2.7 5.2 4.3 6.7 7.3 3.6" stroke="#fff" stroke-width="1.3" fill="none"/></svg>Educated and coached on how to support child</li>
  </ul>

  <div class="abs footer-line"></div>
  <footer class="abs footer">For more information please visit us on: <b>www.quietharboracademy.com</b></footer>

  <svg class="abs globe" width="48" height="48" viewBox="0 0 48 48">
    <circle cx="24" cy="24" r="24" fill="var(--green)"/>
    <circle cx="24" cy="24" r="19" fill="var(--white)"/>
    <g fill="none" stroke="var(--purple)" stroke-width="1.6">
      <circle cx="24" cy="24" r="13"/>
      <ellipse cx="24" cy="24" rx="6" ry="13"/>
      <line x1="24" y1="11" x2="24" y2="37"/>
      <line x1="11" y1="24" x2="37" y2="24"/>
      <line x1="13" y1="17.5" x2="35" y2="17.5"/>
      <line x1="13" y1="30.5" x2="35" y2="30.5"/>
    </g>
  </svg>

</main>
</body>
</html>
```